LedgerNook Project
LedgerNook
Project: LedgerNook Project
LedgerNook Project - Financial Services
Creative Brief
Bright & Fun-filled
Peter Halvik
President
Leave blank
peter@ledgernook.example
www.ledgernook.example
The front should be white with logo, my name, cell phone, email address, and website. Leave address blank because there is no physical address at the moment. List these services with bullet point. (accounting, bookkeeping, and payroll) Please make sure the design meet GlossPrint silk laminate with spot uv because I plan to use them to print in the future. Check link: http://www.glossprint.example/Business-Cards/Silk-Business-Cards-with-Spot-UV-and-Rounded-Corners
I want the back to be a solid color with logo. Check link for what I am looking for: http://www.glossprint.example/Inspiration-Gallery#/gallery/img/images_M.jpg

```html
<!DOCTYPE html>
<html lang="en">
<head>
<meta charset="utf-8">
<title>LedgerNook Business Cards</title>
<link href="https://fonts.googleapis.com/css2?family=Source+Sans+3:wght@400;600;700&display=swap" rel="stylesheet">
<style>
  :root {
    --stage: #e9e6e1;
    --card-white: #ffffff;
    --card-black: #050505;
    --card-blue: #3f97d6;
    --brand-blue: #2f84c8;
    --navy: #1b3a5c;
    --ink: #1a1a1a;
    --shadow: rgba(0, 0, 0, 0.18);
  }
  * { box-sizing: border-box; margin: 0; padding: 0; }
  html, body {
    width: 1200px;
    height: 751px;
    overflow: hidden;
    background: var(--stage);
    font-family: "Source Sans 3", Arial, sans-serif;
  }
  .canvas { position: relative; width: 1200px; height: 751px; }
  .card {
    position: absolute;
    overflow: hidden;
    box-shadow: 0 4px 14px var(--shadow);
  }
  .card--front { left: 324px; top: 53px; width: 456px; height: 264px; background: var(--card-white); }
  .card--back-dark { left: 96px; top: 379px; width: 492px; height: 288px; background: var(--card-black); }
  .card--back-blue { left: 612px; top: 379px; width: 492px; height: 288px; background: var(--card-blue); }

  .brand { display: flex; flex-direction: column; align-items: center; gap: 8px; }
  .brand__name { font-weight: 700; line-height: 1; letter-spacing: -0.5px; white-space: nowrap; }

  .card--front .brand { position: absolute; left: 20px; top: 30px; }
  .card--front .brand__mark { background: var(--brand-blue); width: 34px; height: 34px; }
  .card--front .brand__name { color: var(--brand-blue); font-size: 24px; }

  .holder { position: absolute; left: 22px; top: 136px; color: var(--ink); }
  .holder__name { font-weight: 700; font-size: 14px; line-height: 16px; }
  .holder__title { font-size: 12px; line-height: 14px; }

  .contact {
    position: absolute; left: 286px; top: 136px;
    list-style: none; font-size: 10px; line-height: 12px;
    color: var(--ink); white-space: nowrap;
  }
  .contact b { font-weight: 700; }

  .wave { position: absolute; left: 0; top: 0; width: 456px; height: 264px; }

  .card--back-dark .brand,
  .card--back-blue .brand { position: absolute; left: 0; right: 0; top: 88px; gap: 14px; }
  .card--back-dark .brand__mark,
  .card--back-blue .brand__mark { width: 48px; height: 48px; }
  .card--back-dark .brand__mark { background: var(--brand-blue); }
  .card--back-blue .brand__mark { background: var(--navy); }
  .card--back-dark .brand__name { color: #ffffff; font-size: 46px; }
  .card--back-blue .brand__name { color: var(--navy); font-size: 46px; }

  .site { position: absolute; left: 0; right: 0; bottom: 12px; text-align: center; font-size: 10px; }
  .card--back-dark .site { color: #ffffff; }
  .card--back-blue .site { color: var(--ink); }
</style>
</head>
<body>
<main class="canvas">

  <section class="card card--front" aria-label="Card front">
    <svg class="wave" viewBox="0 0 456 264" aria-hidden="true">
      <path d="M0 228 C110 200 190 244 300 224 C370 212 420 208 456 208 L456 264 L0 264 Z" fill="var(--card-blue)"/>
      <path d="M0 218 C110 190 190 234 300 214 C370 202 420 198 456 196" fill="none" stroke="var(--card-black)" stroke-width="5"/>
    </svg>
    <div class="brand">
      <span class="brand__mark"></span>
      <span class="brand__name">LedgerNook</span>
    </div>
    <div class="holder">
      <p class="holder__name">Peter Halvik</p>
      <p class="holder__title">President</p>
    </div>
    <ul class="contact">
      <li>Leave blank</li>
      <li><b>Cell:</b> 555-010-2274</li>
      <li><b>Email:</b> peter@ledgernook.example</li>
      <li>www.ledgernook.example</li>
    </ul>
  </section>

  <section class="card card--back-dark" aria-label="Card back, black">
    <div class="brand">
      <span class="brand__mark"></span>
      <span class="brand__name">LedgerNook</span>
    </div>
    <p class="site">www.ledgernook.example</p>
  </section>

  <section class="card card--back-blue" aria-label="Card back, blue">
    <div class="brand">
      <span class="brand__mark"></span>
      <span class="brand__name">LedgerNook</span>
    </div>
    <p class="site">www.ledgernook.example</p>
  </section>

</main>
</body>
</html>
```